Solar Carport

Kestrelvale renewables is looking for a flyer promoting our solar carport design in Alberta, BC and Saskatchewan. We call it the Tinderloft. We have specific color pallet. Should be flashy, endorse local manufacturing, and the over all design should have a green feel to it. We would also like to add this to our website. We will offer this design in steel and wood beam frame.

```html
<!DOCTYPE html>
<html lang="en">
<head>
<meta charset="utf-8">
<title>Kestrelvale Renewables – Solar Carport Flyer</title>
<link rel="stylesheet" href="https://fonts.googleapis.com/css2?family=Ubuntu:wght@500;700&family=Arimo:wght@400&display=swap">
<style>
  :root {
    --backdrop: #323232;
    --green: #6cc04a;
    --green-deep: #4f9e34;
    --navy: #253f86;
    --royal: #3f5bb3;
    --title-blue: #3a54a8;
    --black: #000000;
    --white: #ffffff;
    --ink: #111111;
    --sky: #8497a8;
    --sky-low: #6f7f8d;
    --haze: #9a9a98;
    --ground: #262626;
    --timber: #d9822b;
    --panel-dark: #4a4f57;
  }
  * { box-sizing: border-box; margin: 0; padding: 0; }
  html, body { width: 698px; height: 1200px; overflow: hidden; background: var(--backdrop); }
  .flyer {
    position: absolute; left: 0; top: 106px;
    width: 675px; height: 956px;
    transform: scale(1.034); transform-origin: 0 0;
    background: var(--green);
    font-family: "Arimo", Arial, sans-serif;
  }
  .abs { position: absolute; }
  .brand-box {
    left: 8px; top: 8px; width: 162px; height: 122px; background: var(--white);
    display: flex; flex-direction: column; align-items: center; justify-content: center; gap: 8px;
  }
  .brand-mark { width: 34px; height: 34px; border-radius: 50%; background: var(--royal); }
  .brand-name {
    font-family: "Ubuntu", sans-serif; font-weight: 700; font-size: 15px;
    color: var(--royal); text-align: center; line-height: 1.15;
  }
  .headline-box { left: 170px; top: 8px; width: 497px; height: 122px; background: var(--black); }
  .headline {
    left: 48px; top: 22px; font-family: "Ubuntu", sans-serif; font-weight: 700;
    font-size: 35px; line-height: 39px; color: var(--white);
  }
  .headline .accent { color: var(--green); }
  .specialists {
    left: 55px; top: 142px; width: 567px; height: 34px; background: var(--green-deep);
    color: var(--white); font-family: "Ubuntu", sans-serif; font-weight: 700; font-size: 24.5px;
    text-align: center; line-height: 34px; letter-spacing: 0.3px;
  }
  .rule-white { left: 8px; top: 182px; width: 659px; height: 4px; background: var(--white); }
  .tabs { left: 8px; top: 188px; width: 659px; height: 70px; display: flex; }
  .tab {
    flex: 1; color: var(--white); font-family: "Ubuntu", sans-serif; font-weight: 700;
    font-size: 23px; display: flex; align-items: center; justify-content: center; background: var(--navy);
  }
  .tab.is-featured { background: var(--royal); }
  .tab-notes {
    left: 8px; top: 260px; width: 659px; height: 58px; background: var(--white);
    display: flex; align-items: center;
  }
  .note {
    flex: 1; text-align: center; font-size: 14.5px; line-height: 19px; color: var(--ink);
    border-left: 3px solid var(--ink);
  }
  .note:first-child { border-left: none; }
  .more-band { left: 8px; top: 340px; width: 659px; height: 24px; background: var(--green-deep); }
  .more-title {
    left: 100px; top: 327px; width: 475px; height: 32px; background: var(--white);
    color: var(--title-blue); font-family: "Ubuntu", sans-serif; font-weight: 700; font-size: 27px;
    text-align: center; line-height: 32px;
  }
  .gallery { left: 5px; top: 372px; }
  .closing {
    left: 0; top: 835px; width: 675px; height: 52px; background: var(--black);
    display: flex; align-items: center; justify-content: center; gap: 14px;
    color: var(--white); font-family: "Ubuntu", sans-serif; font-weight: 700; font-size: 25px;
  }
  .closing .line { flex: 1; height: 4px; background: var(--white); }
  .contact { left: 0; top: 887px; width: 675px; height: 69px; background: var(--white); }
  .contact-item { display: flex; align-items: center; gap: 12px; font-size: 17.5px; color: var(--ink); line-height: 25px; }
  .phone-item { position: absolute; left: 52px; top: 8px; }
  .web-item { position: absolute; left: 305px; top: 21px; }
  .icon { width: 40px; height: 40px; flex: none; }
</style>
</head>
<body>
  <div class="flyer">
    <div class="abs brand-box">
      <div class="brand-mark"></div>
      <div class="brand-name">Kestrelvale<br>Renewables</div>
    </div>
    <div class="abs headline-box">
      <p class="abs headline">your #1 choice <span class="accent">in</span><br><span class="accent">renewable energy</span></p>
    </div>

    <div class="abs specialists">YOUR RENEWABLE ENERGY SPECIALISTS</div>
    <div class="abs rule-white"></div>

    <div class="abs tabs">
      <div class="tab">PRODUCTS</div>
      <div class="tab is-featured">INVESTISEMENT</div>
      <div class="tab">CUSTOM</div>
    </div>
    <div class="abs tab-notes">
      <p class="note">Grid Tie Micro Generation<br>Solar panels - Off Grid</p>
      <p class="note">Solar power systems are<br>more affordabale than ever</p>
      <p class="note">Every system is<br>individually engineered</p>
    </div>

    <div class="abs more-band"></div>
    <div class="abs more-title">MORE THAN JUST SOLAR PANELS</div>

    <svg class="abs gallery" width="665" height="460" viewBox="0 0 665 460">
      <defs>
        <linearGradient id="timberScene" x1="0" y1="0" x2="0" y2="1">
          <stop offset="0" stop-color="var(--sky)"/>
          <stop offset="0.22" stop-color="var(--sky-low)"/>
          <stop offset="0.36" stop-color="var(--timber)"/>
          <stop offset="0.5" stop-color="#b8742f"/>
          <stop offset="0.62" stop-color="var(--haze)"/>
          <stop offset="0.78" stop-color="#3a3a3a"/>
          <stop offset="1" stop-color="var(--ground)"/>
        </linearGradient>
        <linearGradient id="panelScene" x1="0" y1="0" x2="0" y2="1">
          <stop offset="0" stop-color="var(--haze)"/>
          <stop offset="0.18" stop-color="var(--panel-dark)"/>
          <stop offset="0.55" stop-color="#5a5f67"/>
          <stop offset="0.7" stop-color="#3a3a3a"/>
          <stop offset="1" stop-color="var(--ground)"/>
        </linearGradient>
        <linearGradient id="pairScene" x1="0" y1="0" x2="0" y2="1">
          <stop offset="0" stop-color="var(--sky)"/>
          <stop offset="0.12" stop-color="var(--sky-low)"/>
          <stop offset="0.25" stop-color="var(--timber)"/>
          <stop offset="0.38" stop-color="#c27a30"/>
          <stop offset="0.55" stop-color="var(--haze)"/>
          <stop offset="0.75" stop-color="#333333"/>
          <stop offset="1" stop-color="var(--ground)"/>
        </linearGradient>
      </defs>
      <polygon role="img" aria-label="Rendering of the Tinderloft timber-frame solar carport seen from the side"
               points="0,0 382,0 275,256 0,256" fill="url(#timberScene)"/>
      <polygon role="img" aria-label="Rendering of the Tinderloft carport roof covered in solar panels"
               points="390,0 662,0 662,256 283,256" fill="url(#panelScene)"/>
      <rect role="img" aria-label="Rendering of two Tinderloft timber-frame solar carports over parking spaces"
            x="3" y="264" width="659" height="194" fill="url(#pairScene)"/>
    </svg>

    <div class="abs closing">
      <span class="line"></span>
      <span>We look forward to serving you!</span>
      <span class="line"></span>
    </div>

    <div class="abs contact">
      <div class="contact-item phone-item">
        <svg class="icon" viewBox="0 0 40 40" aria-hidden="true">
          <circle cx="20" cy="20" r="20" fill="var(--green)"/>
          <path d="M13 10c1.5-1 3-.5 3.6.8l1.6 3.4c.5 1.1.1 2.2-.8 2.8l-1.2.8c1 2.7 3.1 5 5.8 6.2l.9-1.1c.7-.9 1.900-1.1 2.9-.5l3.2 1.9c1.2.7 1.5 2.2.6 3.500-1.3 1.9-3.4 2.8-5.7 1.9C17 27.5 12.3 22.5 10.7 16c-.6-2.4.4-4.6 2.3-6z" fill="var(--white)"/>
        </svg>
        <div>403.555.0148<br>780.555.0193</div>
      </div>
      <div class="contact-item web-item">
        <svg class="icon" viewBox="0 0 40 40" aria-hidden="true">
          <circle cx="20" cy="20" r="20" fill="var(--green)"/>
          <g fill="none" stroke="var(--white)" stroke-width="1.8">
            <circle cx="20" cy="20" r="10"/>
            <ellipse cx="20" cy="20" rx="4.5" ry="10"/>
            <line x1="10" y1="20" x2="30" y2="20"/>
            <line x1="12" y1="14" x2="28" y2="14"/>
            <line x1="12" y1="26" x2="28" y2="26"/>
          </g>
        </svg>
        <div>https://kestrelvalerenewables.com/</div>
      </div>
    </div>
  </div>
</body>
</html>
```